Business card design for counselling and psychotherapy practice

I am seeking a business card for a new venture into private practice. I am based in Brisbane Qld Australia. I provide holistic counselling and psychotherapy to individuals and groups.
Some words that describe the underpinnings of this practice would include: being, becoming, awareness, wholeness, contact, safety, acceptance, relationship, gestalt, paradox, interconnected, nature, process.
I would like to see designs that include earth colours.
The overall design should communicate safety and a curiosity of being and becoming.
Target Market(s)
this design is marketed toward women, professionals, lesbian, transgender, mothers
Industry/Entity Type
Safety
Contact Information for Business Card
Willow & Tide
Counselling and Psychotherapy
Maren Olcott
ph: 0417382905
email: maren.willow&tide@quietmail.net
www.willow&tidecounselling&psychotherapy.net
Logo styles of interest
Abstract Logo
Look and feel
Each slider illustrates characteristics of the customer's brand and the style your logo design should communicate.

```html
<!DOCTYPE html>
<html lang="en">
<head>
<meta charset="utf-8">
<title>Willow &amp; Tide – Business Card</title>
<link rel="stylesheet" href="https://fonts.googleapis.com/css2?family=Libre+Baskerville&family=Roboto:wght@300&family=Jost:wght@400&display=swap">
<style>
  :root {
    --mint-deep: #5ef2b4;
    --mint-mid: #8ff7cc;
    --mint-pale: #c4fbe4;
    --band: rgba(70, 205, 160, 0.35);
    --paper: #f4fff9;
    --paper-edge: #dcfcea;
    --white: #ffffff;
    --ink: #5f6c6b;
  }
  html, body {
    margin: 0;
    padding: 0;
    overflow: hidden;
    background: #ffffff;
  }
  .card {
    position: relative;
    width: 1200px;
    height: 741px;
    overflow: hidden;
    background: linear-gradient(125deg, var(--mint-deep) 0%, var(--mint-mid) 45%, var(--mint-pale) 75%, var(--mint-mid) 100%);
  }
  .card__shapes {
    position: absolute;
    inset: 0;
  }
  .brand {
    position: absolute;
    left: 0;
    right: 0;
    top: 202px;
    text-align: center;
    color: var(--white);
  }
  .brand__name {
    margin: 0;
    font-family: "Libre Baskerville", serif;
    font-weight: 400;
    font-size: 82px;
    line-height: 1;
    letter-spacing: 1px;
  }
  .brand__tagline {
    margin: 22px 0 0;
    font-family: "Roboto", sans-serif;
    font-weight: 300;
    font-size: 39px;
    line-height: 1;
    letter-spacing: 1px;
  }
  .contact {
    position: absolute;
    left: 149px;
    top: 476px;
    color: var(--ink);
    font-family: "Jost", sans-serif;
    font-weight: 400;
  }
  .contact__name {
    margin: 0 0 6px;
    font-size: 46px;
    font-weight: 400;
    line-height: 1.1;
  }
  .contact__line {
    margin: 0;
    font-size: 31px;
    line-height: 41px;
  }
</style>
</head>
<body>
  <div class="card">
    <svg class="card__shapes" width="1200" height="741" viewBox="0 0 1200 741" aria-hidden="true">
      <defs>
        <linearGradient id="paperFade" x1="0" y1="0" x2="1" y2="0">
          <stop offset="0" stop-color="var(--paper)"/>
          <stop offset="0.55" stop-color="var(--paper)"/>
          <stop offset="1" stop-color="var(--paper-edge)"/>
        </linearGradient>
      </defs>
      <rect class="title-band" x="0" y="165" width="1200" height="208" fill="var(--band)"/>
      <rect class="title-band__rule" x="0" y="380" width="1200" height="6" fill="rgba(255,255,255,0.45)"/>
      <path class="lower-wave" d="M0 402 C 220 385, 420 385, 560 420 C 760 470, 980 540, 1200 562 L1200 741 L0 741 Z" fill="url(#paperFade)"/>
    </svg>

    <header class="brand">
      <h1 class="brand__name">WILLOW &amp; TIDE</h1>
      <p class="brand__tagline">COUNSELLING AND PSYCHOTHERAPY</p>
    </header>

    <section class="contact">
      <h2 class="contact__name">Maren Olcott</h2>
      <p class="contact__line">ph: 041.738.2905</p>
      <p class="contact__line">email: maren.willowandtide@quietmail.net</p>
      <p class="contact__line">www.willowandtidecounsellingandpsychotherapy.net</p>
    </section>
  </div>
</body>
</html>
```